A spanish dental office Ads

We need a small poster sized Ads in Spanish, which has information as shown in the attached newspaper ads, please also add in office hour information as shown on the website(http://brookvalesmiles-example.com/). Some other info could also be included, such as we provide broad range of dental services for both adult and children. practice logo was attached, the background of the ads do not need to be red.

```html
<!DOCTYPE html>
<html lang="es">
<head>
<meta charset="utf-8">
<title>Brookvale Smiles – Anuncio</title>
<link rel="stylesheet" href="https://fonts.googleapis.com/css2?family=Roboto+Condensed:wght@400;700;900&family=Roboto:wght@400;700;900&display=swap">
<style>
  :root{
    --yellow:#fcc62a;
    --yellow-deep:#f4b417;
    --blue:#1f3b87;
    --red:#e1262d;
    --paper:#ffffff;
    --stage:#ecebe8;
  }
  *{box-sizing:border-box;margin:0;padding:0}
  html,body{width:1200px;height:1148px;overflow:hidden;background:var(--stage)}
  .poster{
    position:absolute;left:260px;top:34px;width:680px;height:1080px;
    background:var(--paper);overflow:hidden;
    font-family:"Roboto Condensed",Arial,sans-serif;
  }
  .top-band{
    position:absolute;left:0;top:0;width:100%;height:261px;
    background:linear-gradient(90deg,var(--yellow),var(--yellow-deep));
  }
  .contact-head{position:absolute;top:30px;left:0;width:100%;text-align:center}
  .contact-head .lang{color:var(--blue);font-weight:700;font-size:23px;letter-spacing:.3px}
  .contact-head .phone{color:var(--red);font-weight:700;font-size:40px;line-height:1.05;letter-spacing:.5px}
  .contact-head .assistant{color:#3b3b3b;font-size:15px;letter-spacing:1.2px}

  .cross{position:absolute;left:182px;top:127px}

  .offer{position:absolute;top:455px;color:var(--red);text-transform:uppercase}
  .offer .price{font-family:"Roboto",Arial,sans-serif;font-size:50px;font-weight:400;line-height:1}
  .offer .label{font-size:19px;line-height:1.12;margin-top:8px}
  .offer--whitening{left:186px}
  .offer--checkup{left:424px}

  .gratis{position:absolute;left:188px;top:582px;width:344px}
  .gratis .word{
    background:var(--blue);color:var(--yellow);height:88px;
    font-family:"Roboto",Arial,sans-serif;font-weight:900;font-size:76px;
    line-height:88px;text-align:center;letter-spacing:3px;
  }
  .gratis .note{
    background:var(--red);color:#fff;text-align:center;text-transform:uppercase;
    font-size:11px;line-height:12px;padding:3px 4px 4px;font-weight:700;
  }
  .insurance{
    position:absolute;left:188px;top:712px;width:344px;text-align:center;
    color:var(--blue);font-weight:700;font-size:13px;text-transform:uppercase;
    padding-bottom:3px;border-bottom:2px solid var(--red);
  }

  .brand{
    position:absolute;left:188px;top:780px;width:344px;
    display:flex;align-items:center;justify-content:center;gap:12px;
  }
  .brand .dot{width:30px;height:30px;border-radius:50%;background:var(--blue)}
  .brand .name{color:var(--blue);font-weight:700;font-size:34px;letter-spacing:.5px;text-transform:uppercase}

  .hours{
    position:absolute;left:200px;top:884px;width:334px;height:34px;
    background:var(--red);color:#fff;font-weight:700;font-size:15px;
    line-height:34px;text-align:center;text-transform:uppercase;
  }
  .address{
    position:absolute;left:330px;top:934px;color:var(--blue);
    font-size:14px;line-height:19px;font-style:normal;
  }
  .address .street{font-weight:700;text-transform:uppercase}
  .address .street span{font-weight:400;text-transform:none}
  .address .line{display:flex;align-items:center;gap:6px;font-size:13.5px}
  .address .line svg{flex:none}
  .bottom-rule{position:absolute;left:0;top:1062px;width:100%;height:8px;background:var(--yellow)}
</style>
</head>
<body>
<main class="poster">
  <div class="top-band"></div>

  <header class="contact-head">
    <p class="lang">HABLAMOS ESPANOL</p>
    <p class="phone">555-014-2290</p>
    <p class="assistant">LUCIA ASISTENTE HISPANA</p>
  </header>

  <svg class="cross" width="316" height="330" viewBox="0 0 316 330" role="img" aria-label="Cruz formada por ilustraciones de instrumentos y productos dentales">
    <path d="M80 0h156v134h80v132h-80v64h-156v-64h-80v-132h80z" fill="#fff"/>
    <path d="M88 8h140v134h80v116h-80v64h-140v-64h-80v-116h80z" fill="var(--blue)"/>
  </svg>

  <div class="offer offer--whitening">
    <p class="price">$99</p>
    <p class="label">Blanqueo<br>Professional</p>
  </div>
  <div class="offer offer--checkup">
    <p class="price">$79</p>
    <p class="label">Diagnostico,<br>Rayos y limpieza</p>
  </div>

  <section class="gratis">
    <p class="word">GRATIS</p>
    <p class="note">Nuevos pacientes con seguro reciben<br>de regalo un cepillo electronico</p>
  </section>
  <p class="insurance">Aceptamos la mayoria de los seguros y medicaid…</p>

  <div class="brand">
    <span class="dot"></span>
    <span class="name">Brookvale Smiles</span>
  </div>

  <p class="hours">Abierto de lunes a sabados</p>

  <address class="address">
    <p class="street">4820, Maple Grove Rd. Suite 210,</p>
    <p class="street">Riverton, NC 27000 <span>(salida 18 de la 12)</span></p>
    <p class="line">
      <svg width="10" height="10" viewBox="0 0 10 10"><rect width="10" height="10" rx="2" fill="var(--blue)"/><circle cx="5" cy="5" r="2.6" fill="none" stroke="#fff" stroke-width="1"/></svg>
      www.brookvalesmiles-example.com
    </p>
    <p class="line">
      <svg width="10" height="10" viewBox="0 0 10 10"><rect width="10" height="10" rx="2" fill="var(--blue)"/><path d="M2 3.2h6v3.6H2z M2 3.2l3 2 3-2" fill="none" stroke="#fff" stroke-width=".9"/></svg>
      info@brookvalesmiles-example.com
    </p>
  </address>

  <div class="bottom-rule"></div>
</main>
</body>
</html>
```